Mobile Window Tinting Business Needs A Website

We are currently looking for a clean, professional, easy to use and well laid out website for our company "Bright Glaze Services"

We offer a mobile automotive window tinting service with a scope for expansion into commercial and residential window tinting in the near future although this will not have to be accommodated for too much.

We are after a minimalist website as the business is designed to simplify what can be a rather time confusing and over complicated process and as such we will need our website to embody that easy of use.

If the same colors, textures and fonts were used from www.drivexa.com.au in a similar layout to www.yardquill.com.au that would be what we were after. our biggest selling points are
-flat pricing
-online booking in 60 seconds
-online payment
-mobile service

All products will have a 5 point guarantee regardless of brand.
i.e lifetime warranty, 99% UV blocking etc

We are also partner with with a charity to promote cancer awareness.

We will need a basic vehicle selections tool (make/model/year) for the customer to obtain pricing.

Our primary colors are black, white and silver/grey but are also open to a light blue/blue being used to break up the palate.
Updates

Hi guys,Just a few additional details.The purpose of this site is toa) instill trust b) enable the customer to buy and buy nowc) make a complicated process extremely simpleTo do this ideally I would like a book now button on 3 places on the home page to emphasize the urgency of booking now.I would also like a least 3 peoples faces on the home pages as people relate to images of people therefore instilling trust.and to have well spaced information so as to not overload the customers with to much reading and not enough action.Another form of inspiration can be http://yardquill.com/ as bright glaze services will be running a very similar model to these guys i.e flat pricing, book in 60 seconds. ideally the design will be a mix between yardquill and drivexa website. Thanks for your input guys, look forward to seeing these designs!! Added Thursday, February 19, 2015

Target Market(s)

Currently our target audience is vehicle owners, automotive dealerships, auction houses and car clubs but all transactions will follow the same process so these markets do not have to be specifically incorporated.

Industry/Entity Type

Residential

Number of Pages Required

3 page

Colors
000000
959595
ffffff
0392cd
0455a3

Requirements
Must have
• Icons/Call to actions buttons for;
• -Get A Price
• -Book Now x 3
• At least 3 images of people on the home page as people relate to people (as well as window tinting obviously)
• Methods of contact should be highly visible which will be via phone, email and online chat.
Nice to have
• Would be nice to have an as featured in section and testemonials section.
Should not have
• Clutter and too much unnecessary place holders & text boxes.

```html
<!DOCTYPE html>
<html lang="en">
<head>
<meta charset="utf-8">
<title>Bright Glaze Services – Mobile Automotive Window Tinting</title>
<link href="https://fonts.googleapis.com/css2?family=Open+Sans:wght@400;600;700&family=Arvo:wght@400;700&family=Oswald:wght@400;500&display=swap" rel="stylesheet">
<style>
:root{
  --black:#000000;
  --grey:#959595;
  --white:#ffffff;
  --blue:#0392cd;
  --navy:#0455a3;
  --ink:#333333;
  --soft:#f1f1f1;
  --line:#dddddd;
  --dark:#2a2a2a;
}
*{box-sizing:border-box;margin:0;padding:0}
html,body{width:1200px;height:3076px;overflow:hidden}
body{font-family:"Open Sans",Arial,sans-serif;color:var(--ink);background:var(--white);font-size:14px;line-height:1.5}
section,header,footer{position:relative;width:1200px}
.btn{display:inline-block;background:var(--blue);color:var(--white);font-weight:600;font-size:15px;padding:10px 26px;border-radius:2px;text-decoration:none}
.btn-white{background:var(--white);color:var(--ink)}
.section-title{text-align:center;font-family:"Oswald",sans-serif;font-size:22px;font-weight:400;color:#555;letter-spacing:.5px}
.section-title b{color:var(--ink);font-weight:500}
.section-title::before,.section-title::after{content:"";display:inline-block;width:60px;height:1px;background:#bbb;vertical-align:middle;margin:0 14px}

/* hero */
.hero{height:680px;background:linear-gradient(160deg,#cfd4d8 0%,#9aa2a8 35%,#4b5157 60%,#1e2124 100%)}
.hero-photo{position:absolute;inset:0}
.topbar{position:absolute;top:0;left:0;right:0;height:112px;background:rgba(255,255,255,.55)}
.brand{position:absolute;left:130px;top:20px;display:flex;align-items:center;gap:12px}
.brand-mark{width:46px;height:46px;background:var(--dark)}
.brand-name{font-family:"Arvo",serif;font-weight:700;font-size:20px;color:var(--dark);line-height:1.15;width:200px}
.contact-row{position:absolute;right:130px;top:14px;display:flex;align-items:center;gap:8px}
.social{width:24px;height:24px;border-radius:50%;background:#555}
.phone{margin-left:12px;font-weight:700;font-size:15px;color:var(--dark);display:flex;align-items:center;gap:6px}
.nav{position:absolute;right:130px;top:56px;display:flex;gap:4px}
.nav a{font-size:14px;color:var(--ink);padding:8px 14px;text-decoration:none;background:rgba(255,255,255,.7)}
.nav a.active{background:var(--blue);color:var(--white)}
.hero-title{position:absolute;right:130px;top:148px;width:480px;text-align:right;font-family:"Arvo",serif;font-weight:700;font-size:36px;line-height:1.3;color:var(--dark)}
.quote-bar{position:absolute;left:0;right:0;bottom:0;height:96px;background:rgba(0,0,0,.55);padding:14px 130px}
.quote-bar h3{font-family:"Oswald",sans-serif;font-weight:400;color:var(--white);font-size:18px;margin-bottom:8px}
.quote-form{display:flex;gap:14px}
.quote-form .field{flex:1;height:34px;background:var(--white);font-size:12px;color:#777;padding:8px 10px}
.quote-form .submit{width:110px;height:34px;background:var(--dark);color:var(--white);font-weight:700;text-align:center;line-height:34px;font-size:13px}

/* welcome */
.welcome{height:260px;padding-top:36px;text-align:center}
.welcome .section-title::before,.welcome .section-title::after{display:none}
.welcome p{width:760px;margin:16px auto 14px;font-size:13px;color:#666}
.welcome .btn{font-size:11px;padding:5px 12px}

/* steps */
.steps{height:320px;display:flex;justify-content:center;gap:60px;padding-top:10px}
.step{width:180px;text-align:center}
.step-icon{height:150px;background:#e4e4e4;display:flex;align-items:center;justify-content:center}
.step-label{background:#555;color:var(--white);font-family:"Oswald",sans-serif;font-size:20px;padding:6px 0}
.step p{font-size:12px;color:#666;margin-top:12px}

/* cta band */
.cta-band{height:120px;background:var(--blue);display:flex;align-items:center;justify-content:space-between;padding:0 130px;color:var(--white)}
.cta-band p{width:760px;font-weight:600;font-size:15px}

/* why */
.why{height:260px;padding-top:34px}
.features{display:flex;justify-content:center;gap:60px;margin-top:40px}
.feature{width:180px;text-align:center;font-size:14px;white-space:nowrap}
.feature-icon{width:80px;height:80px;background:#666;margin:0 auto 16px;display:flex;align-items:center;justify-content:center}
.van{position:absolute;right:0;top:40px;width:190px;height:120px;background:linear-gradient(90deg,#f4f4f4,#e3e3e3)}

/* benefits */
.benefits{height:280px;background:var(--soft);padding-top:26px}
.benefit-list{display:grid;grid-template-columns:270px 270px;gap:18px 40px;margin:36px 0 0 260px;list-style:none}
.benefit-list li{display:flex;align-items:center;gap:10px;font-size:13px;white-space:nowrap}
.portrait{position:absolute;right:220px;top:60px;width:130px;height:220px;background:linear-gradient(180deg,#c9cdd1,#3c4148)}

/* charity */
.charity{height:100px;background:var(--navy);color:var(--white);text-align:center;font-family:"Oswald",sans-serif;font-size:26px;line-height:100px}

/* guarantee */
.guarantee{height:220px;text-align:center;padding-top:34px}
.guarantee h2{font-family:"Oswald",sans-serif;font-weight:500;color:var(--blue);font-size:28px}
.guarantee p{font-size:18px;margin:10px 0 24px}

/* brands */
.brands{height:240px;padding-top:20px}
.brand-band{margin-top:22px;height:150px;background:var(--blue);display:flex;align-items:center;justify-content:center;gap:26px}
.arrow{width:30px;height:30px;border-radius:50%;background:var(--white);display:flex;align-items:center;justify-content:center}
.partner{width:170px;height:90px;background:var(--white);display:flex;align-items:center;justify-content:center;font-weight:700;font-size:20px;color:var(--ink)}

/* testimonials */
.testimonials{height:260px;background:#e9e9e9;padding-top:22px}
.testimonial{display:flex;gap:40px;margin:34px 0 0 170px;width:860px}
.client{text-align:center;width:140px;flex:none;font-size:12px}
.avatar{width:100px;height:100px;border-radius:50%;background:linear-gradient(180deg,#d5d8db,#7c838a);border:4px solid var(--white);margin:0 auto 10px}
.quote{font-size:13px;color:#555;font-style:italic}

/* footer */
.site-footer{height:200px;background:var(--dark);color:#ccc;padding:22px 130px;display:flex;gap:60px;font-size:12px}
.site-footer h4{color:var(--white);font-size:15px;margin-bottom:10px}
.site-footer ul{list-style:none}
.site-footer li{margin-bottom:4px}
.map{width:200px;height:110px;background:linear-gradient(135deg,#e7e2d5,#c9d3c2)}
.footer-brand{margin-left:auto;text-align:center;padding-top:10px}
.footer-brand .mark{width:54px;height:54px;border:2px solid var(--white);margin:0 auto 8px}
.footer-brand span{font-family:"Arvo",serif;color:var(--white);font-size:17px;font-weight:700}
.affiliates{height:100px;background:#111;display:flex;align-items:center;padding:0 130px;gap:22px}
.affiliates h4{font-family:"Oswald",sans-serif;color:var(--white);font-weight:400;font-size:24px;line-height:1.1;width:120px}
.affiliate{width:150px;height:50px;background:var(--white);display:flex;align-items:center;justify-content:center;font-weight:700;font-size:15px}
.copyright{height:36px;background:#000;color:#aaa;font-size:11px;display:flex;align-items:center;justify-content:space-between;padding:0 130px}
.payments{display:flex;gap:6px;align-items:center}
.payments i{width:30px;height:18px;background:#ddd}
</style>
</head>
<body>

<header class="hero">
  <div class="hero-photo" role="img" aria-label="Close-up of a tinted car side window"></div>
  <div class="topbar">
    <div class="brand"><div class="brand-mark"></div><div class="brand-name">Bright Glaze Services</div></div>
    <div class="contact-row">
      <span class="social"></span><span class="social"></span><span class="social"></span><span class="social"></span>
      <span class="phone"><svg width="16" height="16" viewBox="0 0 24 24"><path fill="#2a2a2a" d="M6.6 10.8a15 15 0 0 0 6.6 6.6l2.2-2.2c.3-.3.7-.4 1-.2 1.1.4 2.3.6 3.6.6.6 0 1 .4 1 1V20c0 .6-.4 1-1 1A17 17 0 0 1 3 4c0-.6.4-1 1-1h3.5c.6 0 1 .4 1 1 0 1.3.2 2.5.6 3.6.1.3 0 .7-.2 1z"/></svg>(555) 014-2290</span>
    </div>
    <nav class="nav"><a class="active">Home</a><a>How it Works</a><a>Pricing</a><a>Book Now</a><a>About Us</a></nav>
  </div>
  <h1 class="hero-title">We Offer A Mobile Automotive Window Tinting Service</h1>
  <div class="quote-bar">
    <h3>GET A QUOTE</h3>
    <div class="quote-form">
      <div class="field">Vehicle Type</div><div class="field">MAKE</div><div class="field">MODEL</div><div class="field">YEAR</div><div class="submit">SUBMIT</div>
    </div>
  </div>
</header>

<section class="welcome">
  <h2 class="section-title">WELCOME TO <b>BRIGHT GLAZE SERVICES</b></h2>
  <p>Lorem ipsum dolor sit amet, consectetuer adipiscing elit. Nulla in sollicitudin velit, bibendum velit. Cras vel facilisis ipsum, et venenatis risus. In egestas nunc eleifend quis sollicitudin. Etiam at enim vitae magna volutpat venenatis vitae nonummy diam. Nam nunc velit, tristique a sapien euismod, pulvinar vestibulum dui. Morbi porttitor eu est imperdiet pretium consequat fringilla.</p>
  <a class="btn">READ MORE</a>
</section>

<section class="steps">
  <div class="step">
    <div class="step-icon"><svg width="70" height="70" viewBox="0 0 70 70"><rect width="70" height="70" fill="#0392cd"/><rect x="18" y="20" width="34" height="30" fill="none" stroke="#fff" stroke-width="3"/><line x1="18" y1="28" x2="52" y2="28" stroke="#fff" stroke-width="3"/></svg></div>
    <div class="step-label">BOOK</div>
    <p>Lorem ipsum dolor sit amet consectetuer adipiscing elit. Nulla in sollicitudin.</p>
  </div>
  <div class="step">
    <div class="step-icon"><svg width="70" height="70" viewBox="0 0 70 70"><rect width="70" height="70" fill="#0392cd"/><path d="M20 36l10 10 20-22" fill="none" stroke="#fff" stroke-width="5"/></svg></div>
    <div class="step-label">CONFIRM</div>
    <p>Lorem ipsum dolor sit amet consectetuer adipiscing elit. Nulla in sollicitudin.</p>
  </div>
  <div class="step">
    <div class="step-icon"><svg width="70" height="70" viewBox="0 0 70 70"><rect width="70" height="70" fill="#0392cd"/><circle cx="35" cy="35" r="15" fill="none" stroke="#fff" stroke-width="3"/><path d="M28 38q7 7 14 0" fill="none" stroke="#fff" stroke-width="3"/></svg></div>
    <div class="step-label">RELAX</div>
    <p>Lorem ipsum dolor sit amet consectetuer adipiscing elit. Nulla in sollicitudin.</p>
  </div>
</section>

<section class="cta-band">
  <p>Lorem ipsum dolor sit amet, consectetuer adipiscing elit, sed diam nonummy nibh euismod tincidunt ut laoreet dolore magna aliquam erat volutpat.</p>
  <a class="btn btn-white">Book Now</a>
</section>

<section class="why">
  <h2 class="section-title">WHY <b>CHOOSE US</b></h2>
  <div class="features">
    <div class="feature"><div class="feature-icon"><svg width="40" height="30"><rect x="2" y="4" width="36" height="22" fill="none" stroke="#fff" stroke-width="3"/><circle cx="20" cy="15" r="5" fill="#fff"/></svg></div>Flat Pricing</div>
    <div class="feature"><div class="feature-icon"><svg width="36" height="36"><circle cx="18" cy="18" r="15" fill="none" stroke="#fff" stroke-width="3"/><path d="M18 9v10h7" fill="none" stroke="#fff" stroke-width="3"/></svg></div>Online Booking in 60 Seconds</div>
    <div class="feature"><div class="feature-icon"><svg width="40" height="30"><rect x="2" y="3" width="36" height="24" fill="none" stroke="#fff" stroke-width="3"/><line x1="2" y1="11" x2="38" y2="11" stroke="#fff" stroke-width="4"/></svg></div>Online Payment</div>
    <div class="feature"><div class="feature-icon"><svg width="44" height="30"><rect x="2" y="4" width="26" height="18" fill="#fff"/><path d="M28 10h8l6 7v5H28z" fill="#fff"/><circle cx="10" cy="25" r="4" fill="#fff"/><circle cx="34" cy="25" r="4" fill="#fff"/></svg></div>Mobile Service</div>
  </div>
  <div class="van" role="img" aria-label="Faint outline of a service van"></div>
</section>

<section class="benefits">
  <h2 class="section-title">BENEFITS <b>OF TINTING</b></h2>
  <ul class="benefit-list">
    <li><svg width="16" height="16"><path d="M2 8l4 4 8-9" fill="none" stroke="#959595" stroke-width="2"/></svg>Lorem ipsum dolor sit amet, consectetuer</li>
    <li><svg width="16" height="16"><path d="M2 8l4 4 8-9" fill="none" stroke="#959595" stroke-width="2"/></svg>Lorem ipsum dolor sit amet, consectetuer</li>
    <li><svg width="16" height="16"><path d="M2 8l4 4 8-9" fill="none" stroke="#959595" stroke-width="2"/></svg>Lorem ipsum dolor sit amet</li>
    <li><svg width="16" height="16"><path d="M2 8l4 4 8-9" fill="none" stroke="#959595" stroke-width="2"/></svg>Lorem ipsum dolor sit amet</li>
    <li><svg width="16" height="16"><path d="M2 8l4 4 8-9" fill="none" stroke="#959595" stroke-width="2"/></svg>Lorem ipsum dolor sit amet Lorem is</li>
    <li><svg width="16" height="16"><path d="M2 8l4 4 8-9" fill="none" stroke="#959595" stroke-width="2"/></svg>Lorem ipsum dolor sit amet Lorem is</li>
  </ul>
  <div class="portrait" role="img" aria-label="Portrait of a smiling business man in a suit"></div>
</section>

<section class="charity">We Are Also Partner With A Charity To Promote Cancer Awareness.</section>

<section class="guarantee">
  <h2>100% SATISFACTION GUARANTEED</h2>
  <p>Lorem euismod tincidunt ut laoreet dolore magna aliquam erat volutpat.</p>
  <a class="btn">Book Now</a>
</section>

<section class="brands">
  <h2 class="section-title">BRANDS <b>WE SUPPLY</b></h2>
  <div class="brand-band">
    <span class="arrow"><svg width="10" height="12"><path d="M8 1L2 6l6 5" fill="none" stroke="#0392cd" stroke-width="2"/></svg></span>
    <div class="partner">Northline</div><div class="partner">Vantora</div><div class="partner">Keloro</div><div class="partner">Brista</div>
    <span class="arrow"><svg width="10" height="12"><path d="M2 1l6 5-6 5" fill="none" stroke="#0392cd" stroke-width="2"/></svg></span>
  </div>
</section>

<section class="testimonials">
  <h2 class="section-title">Client <b>Testimonials</b></h2>
  <div class="testimonial">
    <div class="client"><div class="avatar" role="img" aria-label="Client portrait"></div>Mr. Alan Perry</div>
    <p class="quote">“ Lorem ipsum dolor sit amet, consectetuer adipiscing elit. Nulla in sollicitudin velit, bibendum velit. Cras vel facilisis ipsum, et venenatis risus. In egestas nunc eleifend quis sollicitudin. Etiam at enim vitae magna volutpat venenatis vitae nonummy diam. Nam nunc velit, tristique a sapien euismod, pulvinar vestibulum dui. Morbi porttitor eu est imperdiet pretium consequat fringilla. Lorem ipsum dolor sit amet, consectetuer adipiscing elit, sed diam nonummy nibh euismod tincidunt ut laoreet dolore magna aliquam erat volutpat. ”</p>
  </div>
</section>

<footer class="site-footer">
  <div><h4>Quick Links</h4><ul><li>Home</li><li>Pricing</li><li>Book Now</li><li>About Us</li><li>Contact Us</li></ul></div>
  <div><h4>Contact Detail</h4><ul><li>14 Harbour View Road</li><li>Westfield, QLD 4000</li><li>(555) 014-2290</li><li>hello@brightglaze.example</li></ul></div>
  <div><h4>Where We Serve</h4><div class="map" role="img" aria-label="Map of the service area"></div></div>
  <div class="footer-brand"><div class="mark"></div><span>BRIGHT GLAZE SERVICES</span></div>
</footer>

<section class="affiliates">
  <h4>Our Affiliates</h4>
  <div class="affiliate">Northline</div><div class="affiliate">Vantora</div><div class="affiliate">Keloro</div><div class="affiliate">Brista</div><div class="affiliate">Solvane</div>
</section>

<section class="copyright">
  <span>© 2015 BRIGHT GLAZE SERVICES. All Rights Reserved</span>
  <span class="payments">Payment We Accept <i></i><i></i><i></i><i></i></span>
</section>

</body>
</html>
```